New Business Card for our Indoor Golf Training Facility

We are looking for designs for a new business card for our indoor golf training facility. Attached is our logo, our logo with our slogan, and here is our elevator pitch (What makes us different from the others) not sure if all the info will fit on one card, maybe you can condense the elevator pitch? here is the info

Elevator Pitch
We work with serious golfers and those that want to be serious golfers…
to make you better, faster, at all phases of the game…
We use the same state-of-the-art technology as professional golfers…
which produces data sets that shows your improvement in real time.
Our facility is available 24/7 to our members, which allows you to improve on your time.

our website: www.parkvistaswing.com

Target Market(s)

Golfers

Font styles to use
Serif
Sans Serif

Colors
ec1f27
f59195
fbd4d5
919191
d3d3d3
1b1b1b

Requirements
Must have
• our logo or our logo with the slogan, elevator pitch (can be condensed or shortened)

```html
<!DOCTYPE html>
<html lang="en">
<head>
<meta charset="utf-8">
<title>Park Vista Swing – Business Card</title>
<link href="https://fonts.googleapis.com/css2?family=Roboto:wght@400;500;700&family=Roboto+Condensed:wght@700&display=swap" rel="stylesheet">
<style>
  :root {
    --brand-red: #ec1f27;
    --card-black: #222222;
    --stage: #2a2a2a;
    --text-grey: #5a5a5a;
    --soft-grey: #d3d3d3;
    --paper: #f7f7f7;
    --white: #ffffff;
  }
  * { box-sizing: border-box; margin: 0; padding: 0; }
  html, body { width: 1200px; height: 900px; overflow: hidden; }
  body {
    background: var(--stage);
    font-family: "Roboto", Arial, sans-serif;
    position: relative;
  }
  .card {
    position: absolute;
    left: 280px;
    width: 640px;
    height: 366px;
    border-radius: 4px;
    box-shadow: 0 10px 30px rgba(0,0,0,.45);
  }
  /* Front */
  .card-front {
    top: 50px;
    background: var(--paper);
    text-align: center;
    padding-top: 64px;
  }
  .brand-name {
    font-size: 44px;
    font-weight: 700;
    color: var(--brand-red);
    line-height: 1;
  }
  .slogan {
    margin-top: 8px;
    font-size: 15px;
    color: var(--brand-red);
    letter-spacing: .3px;
  }
  .pitch-title {
    margin-top: 24px;
    font-size: 17px;
    font-weight: 700;
    color: var(--brand-red);
    letter-spacing: .5px;
  }
  .pitch {
    margin: 8px auto 0;
    width: 600px;
    font-size: 13.5px;
    line-height: 1.4;
    color: var(--text-grey);
    font-weight: 500;
  }
  /* Back */
  .card-back {
    top: 470px;
    background: var(--card-black);
    color: var(--white);
  }
  .person {
    position: absolute;
    right: 360px;
    top: 100px;
    text-align right;
    text-align: right;
  }
  .person-name {
    font-family: "Roboto Condensed", "Arial Narrow", sans-serif;
    font-weight: 700;
    font-size: 36px;
    color: var(--brand-red);
    line-height: 1;
  }
  .person-role {
    margin-top: 4px;
    font-size: 16px;
    font-weight: 500;
    color: var(--white);
  }
  .divider {
    position: absolute;
    left: 298px;
    top: 92px;
    width: 2px;
    height: 84px;
    background: var(--soft-grey);
  }
  .contacts {
    position: absolute;
    left: 322px;
    top: 100px;
    list-style: none;
    font-size: 16px;
    font-weight: 500;
    line-height: 1.4;
  }
  .contacts li { display: flex; align-items: center; gap: 8px; }
  .contacts svg { width: 14px; height: 14px; flex: none; }
  .icon-fill { fill: var(--brand-red); }
  .icon-line { fill: none; stroke: var(--card-black); stroke-width: 2; }
  .address {
    position: absolute;
    left: 60px;
    top: 262px;
    display: flex;
    align-items: center;
    gap: 8px;
    font-size: 17px;
    font-weight: 500;
  }
  .address svg { width: 14px; height: 18px; fill: var(--brand-red); }
</style>
</head>
<body>
  <section class="card card-front">
    <h2 class="brand-name">Park Vista Swing</h2>
    <p class="slogan">Par Is Good. Under Is Better. Be Better.</p>
    <h3 class="pitch-title">ELEVATOR PITCH :</h3>
    <p class="pitch">
      We work with serious golfers and those that want to be serious golfers…<br>
      to make you better, faster, at all phases of the game…<br>
      We use the same state-of-the-art technology as professional golfers…<br>
      which produces data sets that shows your improvement in real time.<br>
      Our facility is available 24/7 to our members, which allows you to improve on your time.
    </p>
  </section>

  <section class="card card-back">
    <div class="person">
      <h1 class="person-name">DANIEL REYES</h1>
      <p class="person-role">CEO/FOUNDER</p>
    </div>
    <div class="divider"></div>
    <ul class="contacts">
      <li>
        <svg viewBox="0 0 24 24"><path class="icon-fill" d="M6.6 10.8a15 15 0 0 0 6.6 6.6l2.2-2.2a1 1 0 0 1 1-.25 11.4 11.4 0 0 0 3.6.57 1 1 0 0 1 1 1V20a1 1 0 0 1-1 1A17 17 0 0 1 3 4a1 1 0 0 1 1-1h3.5a1 1 0 0 1 1 1c0 1.25.2 2.45.57 3.57a1 1 0 0 1-.25 1z"/></svg>
        513-555-0172
      </li>
      <li>
        <svg viewBox="0 0 24 24"><rect class="icon-fill" x="2" y="5" width="20" height="14" rx="1"/><path class="icon-line" d="M3 6l9 7 9-7"/></svg>
        info@parkvistaswing.com
      </li>
      <li>
        <svg viewBox="0 0 24 24"><circle class="icon-fill" cx="12" cy="12" r="10"/><path class="icon-line" d="M2 12h20M12 2c-4 5-4 15 0 20M12 2c4 5 4 15 0 20"/></svg>
        parkvistaswing.com
      </li>
    </ul>
    <p class="address">
      <svg viewBox="0 0 24 32"><path d="M12 0a12 12 0 0 0-12 12c0 9 12 20 12 20s12-11 12-20A12 12 0 0 0 12 0zm0 17a5 5 0 1 1 0-10 5 5 0 0 1 0 10z"/></svg>
      1480 Linden Ridge Rd. Unit B4, Maple Falls, OH 45099
    </p>
  </section>
</body>
</html>
```